Namecard Designs+Logo for a High End Automobile Company

We need a new business card for our company called Velta Motorhof.

www.veltamotorhof.example.sg
Our new website will be up in 2.5 months time.

We sell used and brand new continental cars like Korvane, QTL, Dravell, Solbrini and etc. Currently we are operating from 2 offices in Singapore and United Kingdom.

We want a design which is serious. We are open to colours but try to keep it at a maximum of 3 colours.

We prefer something simple and minimal. We are open to 2 sides printing or even 2 sided namecards. Both UK and Singapore company offices address must be in; either side by side, front and back, or even 2 sided cards.

The logo can be a text logo, emblem, abstract, pictorial or combination.

We are printing with Pribo.com so please kindly follow the printing guideline.

http://uk.pribo.example/help/faq/templates-and-guidelines.html

Rich and Car Enthusiasts

Printing

Must have
• Our 2 offices; UK and Singapore.

Our slogan which is " The Automobile Specialist"
Should not have
• Not more than 3 colours

```html
<!DOCTYPE html>
<html lang="en">
<head>
<meta charset="utf-8">
<title>Velta Motorhof — Business Card</title>
<link rel="stylesheet" href="https://fonts.googleapis.com/css2?family=Questrial&display=swap">
<style>
  :root {
    --backdrop: #e9e9e9;
    --card: #0d0d0d;
    --ink-blue: #9fd3f7;
    --ink-light: #cfe6f7;
    --rule-glow: #3fa9ef;
  }
  * { margin: 0; padding: 0; box-sizing: border-box; }
  html, body {
    width: 1200px; height: 828px; overflow: hidden;
    background: var(--backdrop);
    font-family: "Questrial", sans-serif;
  }
  .card {
    position: absolute;
    top: 238px;
    width: 522px; height: 347px;
    background: var(--card);
    border-radius: 22px;
  }
  .card--front { left: 70px; }
  .card--back  { left: 603px; }

  .wordmark {
    position: absolute;
    left: 0; right: 0; top: 155px;
    text-align: center;
    color: var(--ink-blue);
  }
  .wordmark__name {
    font-size: 40px;
    line-height: 1;
    letter-spacing: 1px;
  }
  .wordmark__slogan {
    margin-top: 10px;
    font-size: 12.5px;
    letter-spacing: 5px;
  }

  .contact {
    position: absolute;
    left: 148px; top: 130px;
    color: var(--ink-blue);
  }
  .contact__name { font-size: 15px; line-height: 19px; }
  .contact__title { font-size: 11.5px; line-height: 16px; color: var(--ink-light); }
  .contact__rule {
    position: absolute;
    left: 93px; top: 175px;
    width: 330px; height: 3px;
  }
  .details {
    position: absolute;
    left: 148px; top: 183px;
    font-size: 10.5px;
    line-height: 13.8px;
    color: var(--ink-light);
  }
  .details__offices { display: flex; }
  .details__office { width: 118px; }
  .details__office--uk { width: auto; }
  .details__row { display: flex; }
  .details__label { width: 118px; }
</style>
</head>
<body>
  <section class="card card--front">
    <div class="wordmark">
      <div class="wordmark__name">Velta Motorhof</div>
      <div class="wordmark__slogan">The Automobile Specialist</div>
    </div>
  </section>

  <section class="card card--back">
    <div class="contact">
      <div class="contact__name">Owen Hartley</div>
      <div class="contact__title">Sales Consultant</div>
    </div>
    <svg class="contact__rule" viewBox="0 0 330 3" preserveAspectRatio="none" aria-hidden="true">
      <defs>
        <linearGradient id="ruleGlow" x1="0" x2="1" y1="0" y2="0">
          <stop offset="0" stop-color="#3fa9ef" stop-opacity="0"/>
          <stop offset="0.35" stop-color="#3fa9ef"/>
          <stop offset="0.6" stop-color="#bfe6ff"/>
          <stop offset="1" stop-color="#3fa9ef" stop-opacity="0"/>
        </linearGradient>
      </defs>
      <rect width="330" height="3" fill="url(#ruleGlow)"/>
    </svg>
    <div class="details">
      <div class="details__offices">
        <div class="details__office">
          <div>Retail Division</div>
          <div>8 Marlow Quay,</div>
          <div>Harbour Point, #03-02,</div>
          <div>Singapore 018955</div>
        </div>
        <div class="details__office details__office--uk">
          <div>UK Office</div>
          <div>22 Aldwyn Street,</div>
          <div>Brackley House, Suite 4,</div>
          <div>London EC2A 4NT</div>
        </div>
      </div>
      <div class="details__row"><span class="details__label">Tel:</span><span>65310000111</span></div>
      <div class="details__row"><span class="details__label">Fax:</span><span>6520000222</span></div>
      <div class="details__row"><span class="details__label">Mobile:</span><span>6590000333</span></div>
      <div class="details__row"><span class="details__label">Email:</span><span>hartley.o@veltamotorhof.example.sg</span></div>
      <div class="details__row"><span class="details__label">Website:</span><span>www.veltamotorhof.example.sg</span></div>
    </div>
  </section>
</body>
</html>
```